Dig for Marble! Create PowerPoint Template for FlowMarble!

We've just merged two companies into one. Now, we need some nice PowerPoint-Templates for presentations. Please have a look at www.flowmarble-example.com to see our logo and learn about, what we do. On our website, you can also see the colors and the style, we are using.

To better show, how one of our presentations looks like, I uploaded an anonymised presentation, we prepared for a customer. But the new design should be more sophisticated and modern.

Target Market(s)

Business-to-Busines

Industry/Entity Type

Business Software

Font styles to use
Sans Serif

Requirements
Must have
• Design must fit to the overall design of our website: www.flowmarble-example.com
• The ratio should bei 16:9 and NOT the old 4:3.
Nice to have
• Professional, but personal touch.

```html
<!DOCTYPE html>
<html lang="en">
<head>
<meta charset="utf-8">
<title>FlowMarble Presentation Template</title>
<link href="https://fonts.googleapis.com/css2?family=Montserrat:wght@400;500;600;700&family=Open+Sans:wght@400;600&display=swap" rel="stylesheet">
<style>
  :root{
    --canvas:#3b3b3b;
    --blue:#1b8ce0;
    --blue-deep:#1477c4;
    --navy:#2f4a6a;
    --ink:#2e3640;
    --grey:#8a8a8a;
    --grey-light:#c4c4c4;
    --tint:#e4f1fb;
    --white:#ffffff;
    --body:#6b7580;
  }
  *{margin:0;padding:0;box-sizing:border-box}
  html,body{width:1200px;height:1200px;overflow:hidden;background:var(--canvas)}
  body{position:relative;font-family:"Open Sans",Arial,sans-serif;color:var(--ink)}
  .slide{position:absolute;width:356px;height:200px;background:var(--white);overflow:hidden}
  .a{position:absolute}
  .col1{left:48px}.col2{left:422px}.col3{left:796px}
  .row1{top:50px}.row2{top:275px}.row3{top:501px}.row4{top:726px}.row5{top:951px}

  .logo{position:absolute;display:flex;align-items:center;gap:4px;font:600 8.5px "Montserrat",sans-serif;color:var(--ink);letter-spacing:.1px}
  .logo .mark{width:9px;height:9px;background:var(--blue)}
  .logo.tl{left:18px;top:15px}
  .logo.tr{right:18px;top:15px}
  .logo.big{font-size:26px;gap:10px;color:var(--ink);left:0;right:0;justify-content:center}
  .logo.big .mark{width:26px;height:26px;background:var(--white)}
  .htitle{position:absolute;top:15px;font:600 8px "Montserrat",sans-serif;color:var(--navy);border-bottom:1px solid var(--navy);padding-bottom:1px}
  .htitle.r{right:18px}.htitle.l{left:16px}

  .hex{clip-path:polygon(50% 0,100% 25%,100% 75%,50% 100%,0 75%,0 25%)}
  .tiny{font-size:3.6px;line-height:5.2px;color:var(--body)}
  .tiny.w{color:#e6f2fc}
  .dot{position:absolute;left:50%;top:50%;width:5px;height:5px;margin:-2.5px 0 0 -2.5px;border-radius:50%;background:var(--white)}

  .bullet .icon{position:absolute;width:19px;height:21px}
  .bullet .t{position:absolute;left:32px;top:-1px;width:120px;font:600 5.4px "Montserrat",sans-serif;color:var(--navy)}
  .bullet .b{position:absolute;left:32px;top:6px;width:118px}
  .bullet.c2 .t{color:var(--blue)}
  .bullet.c3 .t{color:#666}
  .bullet.c4 .t{color:#aaa}
  .c1 .icon{background:var(--navy)}.c2 .icon{background:var(--blue)}.c3 .icon{background:var(--grey)}.c4 .icon{background:var(--grey-light)}
  .pct{position:absolute;font:500 5px "Montserrat",sans-serif;color:#777}

  .agenda .icon{position:absolute;width:16px;height:18px;background:var(--blue)}
  .agenda .t{position:absolute;left:24px;top:1px;width:120px;font:500 8px "Montserrat",sans-serif;color:var(--ink)}
  .agenda .time{position:absolute;left:24px;top:12px;font-size:3.6px;color:var(--blue)}
  .agenda .b{position:absolute;left:24px;top:12px;width:96px}
  .agenda .b.lower{top:17px}
  .agenda.inv .icon{background:var(--white)}
  .agenda.inv .icon .dot{background:var(--blue)}
  .agenda.inv .t{color:var(--white)}

  .band{position:absolute;left:0;width:100%}
  .blue-fill{background:var(--blue)}
  .tint-fill{background:var(--tint)}
  .center-text{text-align:center}
  .sec-title{font:600 8px "Montserrat",sans-serif;color:var(--ink)}
  .rule{width:12px;height:1px;background:var(--blue);margin:3px auto 0}
</style>
</head>
<body>

<!-- 1 Title -->
<section class="slide col1 row1" style="background:var(--blue)">
  <div class="logo big" style="top:72px"><span class="mark"></span>FlowMarble</div>
  <div class="band" style="top:146px;height:32px;background:var(--white)"></div>
  <div class="a center-text" style="left:0;right:0;top:149px;font:600 14px 'Montserrat',sans-serif;color:var(--blue)">Your Title Here</div>
  <div class="a center-text" style="left:0;right:0;top:167px;font-size:7.5px;color:var(--ink)">Your Subtitle Here</div>
</section>

<!-- 2 Bullet & Chart -->
<section class="slide col2 row1">
  <div class="logo tl"><span class="mark"></span>FlowMarble</div>
  <div class="htitle r">Bullet &amp; Chart Area</div>
  <svg class="a" style="left:34px;top:63px" width="100" height="100" viewBox="0 0 100 100">
    <g transform="rotate(-90 50 50)" fill="none" stroke-width="14">
      <circle cx="50" cy="50" r="36" stroke="var(--navy)" stroke-dasharray="113.1 226.2"/>
      <circle cx="50" cy="50" r="36" stroke="var(--grey-light)" stroke-dasharray="28.27 226.2" stroke-dashoffset="-113.1"/>
      <circle cx="50" cy="50" r="36" stroke="var(--grey)" stroke-dasharray="28.27 226.2" stroke-dashoffset="-141.37"/>
      <circle cx="50" cy="50" r="36" stroke="var(--blue)" stroke-dasharray="56.55 226.2" stroke-dashoffset="-169.65"/>
    </g>
  </svg>
  <span class="pct" style="left:31px;top:71px">25 %</span>
  <span class="pct" style="left:138px;top:99px">50 %</span>
  <span class="pct" style="left:18px;top:131px">12.5 %</span>
  <span class="pct" style="left:50px;top:162px;color:#aaa">12.5 %</span>
  <div class="a bullet c1" style="left:179px;top:56px"><div class="icon hex"><span class="dot"></span></div><div class="t">Your Text Here</div><p class="b tiny">Short supporting copy for this point goes here, kept brief to fit two or three lines.</p></div>
  <div class="a bullet c2" style="left:179px;top:88px"><div class="icon hex"><span class="dot"></span></div><div class="t">Your Text Here</div><p class="b tiny">Short supporting copy for this point goes here, kept brief to fit two or three lines.</p></div>
  <div class="a bullet c3" style="left:179px;top:119px"><div class="icon hex"><span class="dot"></span></div><div class="t">Your Text Here</div><p class="b tiny">Short supporting copy for this point goes here, kept brief to fit two or three lines.</p></div>
  <div class="a bullet c4" style="left:179px;top:151px"><div class="icon hex"><span class="dot"></span></div><div class="t">Your Text Here</div><p class="b tiny">Short supporting copy for this point goes here, kept brief to fit two or three lines.</p></div>
</section>

<!-- 3 Experience -->
<section class="slide col3 row1">
  <div class="logo tl"><span class="mark"></span>FlowMarble</div>
  <div class="htitle r">Experience</div>
  <div class="band tint-fill" style="top:37px;height:49px"></div>
  <div class="a center-text sec-title" style="left:0;right:0;top:43px">Our Experience</div>
  <p class="a tiny center-text" style="left:40px;right:40px;top:57px">We have delivered process insight for clients across many sectors, helping teams turn raw system data into clear views of how their work really flows and where it can be improved day by day.</p>
  <div class="a hex" style="left:37px;top:103px;width:48px;height:54px;background:var(--blue)"><div class="hex" role="img" aria-label="Healthcare photo: doctor's coat and stethoscope" style="margin:2px;width:44px;height:50px;background:linear-gradient(160deg,#eef2f6,#9fb3c6)"></div></div>
  <div class="a hex" style="left:94px;top:103px;width:48px;height:54px;background:var(--blue)"><div class="hex" role="img" aria-label="Transport and logistics photo: shipping containers" style="margin:2px;width:44px;height:50px;background:linear-gradient(160deg,#f0a35a,#b8501c)"></div></div>
  <div class="a hex" style="left:153px;top:103px;width:48px;height:54px;background:var(--blue)"><div class="hex" role="img" aria-label="Media photo: film reels" style="margin:2px;width:44px;height:50px;background:linear-gradient(160deg,#f59a3a,#a8401a)"></div></div>
  <div class="a hex" style="left:211px;top:103px;width:48px;height:54px;background:var(--blue)"><div class="hex" role="img" aria-label="Insurance photo: building against sky" style="margin:2px;width:44px;height:50px;background:linear-gradient(160deg,#dce8f4,#8aa6c4)"></div></div>
  <div class="a hex" style="left:269px;top:103px;width:48px;height:54px;background:var(--blue)"><div class="hex" role="img" aria-label="High tech photo: circuit board" style="margin:2px;width:44px;height:50px;background:linear-gradient(160deg,#8a6a3a,#3d4a2a)"></div></div>
  <div class="a center-text" style="left:31px;width:60px;top:162px;font:500 5px 'Montserrat',sans-serif">Healthcare</div>
  <div class="a center-text" style="left:88px;width:60px;top:162px;font:500 5px/7px 'Montserrat',sans-serif">Transport<br>&amp; logistics</div>
  <div class="a center-text" style="left:147px;width:60px;top:162px;font:500 5px 'Montserrat',sans-serif">Media</div>
  <div class="a center-text" style="left:205px;width:60px;top:162px;font:500 5px 'Montserrat',sans-serif">Insurance</div>
  <div class="a center-text" style="left:263px;width:60px;top:162px;font:500 5px 'Montserrat',sans-serif">High tech</div>
</section>

<!-- 4 Agenda -->
<section class="slide col1 row2">
  <div class="logo tl"><span class="mark"></span>FlowMarble</div>
  <div class="htitle r">Our Agenda</div>
  <div class="a agenda" style="left:34px;top:55px"><div class="icon hex"><span class="dot"></span></div><div class="t">Agenda One</div><div class="time">10.00</div><p class="b lower tiny">Short note about this agenda item, kept brief to fit within three small lines of copy.</p></div>
  <div class="a agenda" style="left:173px;top:55px"><div class="icon hex"><span class="dot"></span></div><div class="t">Agenda Three</div><div class="time">10.00</div><p class="b lower tiny">Short note about this agenda item, kept brief to fit within three small lines of copy.</p></div>
  <div class="a agenda" style="left:34px;top:103px"><div class="icon hex"><span class="dot"></span></div><div class="t">Agenda Two</div><div class="time">10.00</div><p class="b lower tiny">Short note about this agenda item, kept brief to fit within three small lines of copy.</p></div>
  <div class="a agenda" style="left:173px;top:103px"><div class="icon hex"><span class="dot"></span></div><div class="t">Agenda Four</div><div class="time">10.00</div><p class="b lower tiny">Short note about this agenda item, kept brief to fit within three small lines of copy.</p></div>
</section>

<!-- 5 About Us -->
<section class="slide col2 row2">
  <div class="htitle l">About Us</div>
  <div class="logo tr"><span class="mark"></span>FlowMarble</div>
  <div class="a center-text sec-title" style="left:0;right:0;top:37px">What do we do?</div>
  <div class="a rule" style="left:172px;top:48px;margin:0"></div>
  <p class="a tiny center-text" style="left:50px;right:50px;top:54px">We bring the platform into your organisation with your staff and our consultants, with a clear focus on better processes. We work in a lean and agile way so that lasting value comes quickly.</p>
  <div class="band tint-fill" style="top:81px;height:100px"></div>
  <div class="a" style="left:27px;top:94px;width:60px">
    <div class="hex" style="width:28px;height:31px;margin:0 auto;background:var(--blue);position:relative"><span class="dot"></span></div>
    <div class="center-text" style="font:600 4.2px 'Montserrat',sans-serif;color:var(--blue);margin-top:4px">Extract</div>
    <p class="tiny center-text" style="font-size:3.2px;line-height:4.8px;margin-top:2px">Data is drawn from many business systems, then cleaned and turned into useful facts that were out of reach before.</p>
  </div>
  <div class="a" style="left:110px;top:94px;width:60px">
    <div class="hex" style="width:28px;height:31px;margin:0 auto;background:var(--blue);position:relative"><span class="dot"></span></div>
    <div class="center-text" style="font:600 4.2px 'Montserrat',sans-serif;color:var(--blue);margin-top:4px">Visualise</div>
    <p class="tiny center-text" style="font-size:3.2px;line-height:4.8px;margin-top:2px">Data is drawn from many business systems, then cleaned and turned into useful facts that were out of reach before.</p>
  </div>
  <div class="a" style="left:192px;top:94px;width:60px">
    <div class="hex" style="width:28px;height:31px;margin:0 auto;background:var(--blue);position:relative"><span class="dot"></span></div>
    <div class="center-text" style="font:600 4.2px 'Montserrat',sans-serif;color:var(--blue);margin-top:4px">Analyse</div>
    <p class="tiny center-text" style="font-size:3.2px;line-height:4.8px;margin-top:2px">Data is drawn from many business systems, then cleaned and turned into useful facts that were out of reach before.</p>
  </div>
  <div class="a" style="left:275px;top:94px;width:60px">
    <div class="hex" style="width:28px;height:31px;margin:0 auto;background:var(--blue);position:relative"><span class="dot"></span></div>
    <div class="center-text" style="font:600 4.2px 'Montserrat',sans-serif;color:var(--blue);margin-top:4px">Improve</div>
    <p class="tiny center-text" style="font-size:3.2px;line-height:4.8px;margin-top:2px">Data is drawn from many business systems, then cleaned and turned into useful facts that were out of reach before.</p>
  </div>
</section>

<!-- 6 Coffee Break -->
<section class="slide col3 row2">
  <div class="a" role="img" aria-label="Blue-tinted photo of a doctor with a stethoscope" style="inset:0;background:linear-gradient(110deg,#5aa8e4,#2f8fdc 50%,#3d98e0)"></div>
  <svg class="a" style="left:166px;top:50px" width="30" height="30" viewBox="0 0 30 30" fill="none" stroke="#fff" stroke-width="1.4" stroke-linecap="round">
    <path d="M11 2c-2 2 2 3 0 5M15 2c-2 2 2 3 0 5"/>
    <path d="M5 11h18v7a7 7 0 0 1-7 7h-4a7 7 0 0 1-7-7z"/>
    <path d="M23 13h2a3 3 0 0 1 0 6h-2"/>
    <path d="M4 27h20"/>
  </svg>
  <div class="a" style="left:228px;top:92px;right:0;height:20px;background:var(--navy)"></div>
  <div class="a" style="left:165px;top:93px;font:500 14px 'Montserrat',sans-serif;color:#fff"><b style="font-weight:700">COFFEE</b> BREAK</div>
</section>

<!-- 7 Title Goes Here -->
<section class="slide col1 row3">
  <div class="a" role="img" aria-label="Photo of business people in suits talking at a table" style="left:128px;top:0;right:0;bottom:0;background:linear-gradient(120deg,#e8ecef,#9aa3ac 55%,#c9ced3)"></div>
  <div class="logo tl"><span class="mark"></span>FlowMarble</div>
  <div class="a" style="left:0;top:39px;width:222px;height:131px;background:var(--blue);opacity:.95"></div>
  <div class="a" style="left:23px;top:56px;font:600 7.5px 'Montserrat',sans-serif;color:#fff">Title Goes Here</div>
  <p class="a tiny w" style="left:23px;top:70px;width:190px">Here is a short block of body copy for this slide. It explains the main idea in a few plain sentences and leaves room for detail. Keep the message clear, brief and easy to scan for the reader in the room.</p>
  <p class="a tiny w" style="left:23px;top:107px;width:190px">Here is a short block of body copy for this slide. It explains the main idea in a few plain sentences and leaves room for detail. Keep the message clear, brief and easy to scan for the reader in the room.</p>
</section>

<!-- 8 Bullet & Chart -->
<section class="slide col2 row3">
  <div class="htitle l">Bullet &amp; Chart Area</div>
  <div class="logo tr"><span class="mark"></span>FlowMarble</div>
  <svg class="a" style="left:34px;top:63px" width="100" height="100" viewBox="0 0 100 100">
    <g transform="rotate(-90 50 50)" fill="none" stroke-width="14">
      <circle cx="50" cy="50" r="36" stroke="var(--navy)" stroke-dasharray="113.1 226.2"/>
      <circle cx="50" cy="50" r="36" stroke="var(--grey-light)" stroke-dasharray="28.27 226.2" stroke-dashoffset="-113.1"/>
      <circle cx="50" cy="50" r="36" stroke="var(--grey)" stroke-dasharray="28.27 226.2" stroke-dashoffset="-141.37"/>
      <circle cx="50" cy="50" r="36" stroke="var(--blue)" stroke-dasharray="56.55 226.2" stroke-dashoffset="-169.65"/>
    </g>
  </svg>
  <span class="pct" style="left:31px;top:71px">25 %</span>
  <span class="pct" style="left:138px;top:99px">50 %</span>
  <span class="pct" style="left:18px;top:131px">12.5 %</span>
  <span class="pct" style="left:50px;top:162px;color:#aaa">12.5 %</span>
  <div class="a bullet c1" style="left:179px;top:56px"><div class="icon hex"><span class="dot"></span></div><div class="t">Your Text Here</div><p class="b tiny">Short supporting copy for this point goes here, kept brief to fit two or three lines.</p></div>
  <div class="a bullet c2" style="left:179px;top:88px"><div class="icon hex"><span class="dot"></span></div><div class="t">Your Text Here</div><p class="b tiny">Short supporting copy for this point goes here, kept brief to fit two or three lines.</p></div>
  <div class="a bullet c3" style="left:179px;top:119px"><div class="icon hex"><span class="dot"></span></div><div class="t">Your Text Here</div><p class="b tiny">Short supporting copy for this point goes here, kept brief to fit two or three lines.</p></div>
  <div class="a bullet c4" style="left:179px;top:151px"><div class="icon hex"><span class="dot"></span></div><div class="t">Your Text Here</div><p class="b tiny">Short supporting copy for this point goes here, kept brief to fit two or three lines.</p></div>
</section>

<!-- 9 Agenda grid -->
<section class="slide col3 row3">
  <div class="logo tl"><span class="mark"></span>FlowMarble</div>
  <div class="htitle r">Our Agenda</div>
  <div class="a agenda" style="left:50px;top:42px"><div class="icon hex"><span class="dot"></span></div><div class="t">Lorem Ipsum</div><p class="b tiny">Short note about this agenda item, kept brief to fit within three small lines of copy.</p></div>
  <div class="a agenda" style="left:188px;top:42px"><div class="icon hex"><span class="dot"></span></div><div class="t">Lorem Ipsum</div><p class="b tiny">Short note about this agenda item, kept brief to fit within three small lines of copy.</p></div>
  <div class="a agenda" style="left:50px;top:90px"><div class="icon hex"><span class="dot"></span></div><div class="t">Agenda Two</div><p class="b tiny">Short note about this agenda item, kept brief to fit within three small lines of copy.</p></div>
  <div class="a agenda" style="left:188px;top:90px"><div class="icon hex"><span class="dot"></span></div><div class="t">Lorem Ipsum</div><p class="b tiny">Short note about this agenda item, kept brief to fit within three small lines of copy.</p></div>
  <div class="a agenda" style="left:50px;top:137px"><div class="icon hex"><span class="dot"></span></div><div class="t">Lorem Ipsum</div><p class="b tiny">Short note about this agenda item, kept brief to fit within three small lines of copy.</p></div>
  <div class="a agenda" style="left:188px;top:137px"><div class="icon hex"><span class="dot"></span></div><div class="t">Lorem Ipsum</div><p class="b tiny">Short note about this agenda item, kept brief to fit within three small lines of copy.</p></div>
</section>

<!-- 10 Vision & Mission -->
<section class="slide col1 row4">
  <div class="logo tl"><span class="mark"></span>FlowMarble</div>
  <div class="htitle r">Our Vision And Mission</div>
  <div class="band blue-fill" style="top:48px;height:124px"></div>
  <div class="a" style="left:38px;top:62px;font:600 7.5px 'Montserrat',sans-serif;color:#fff">Our Vision</div>
  <div class="a" style="left:38px;top:73px;font-size:6px;color:#e6f2fc">Platform for improvement</div>
  <p class="a tiny w" style="left:38px;top:85px;width:125px">Here is a short block of body copy for this slide. It explains the main idea in a few plain sentences and leaves room for detail. Keep the message clear, brief and easy to scan for the reader in the room.</p>
  <div class="a" style="left:185px;top:62px;font:600 7.5px 'Montserrat',sans-serif;color:#fff">Our Mission</div>
  <div class="a" style="left:185px;top:73px;font-size:6px;color:#e6f2fc">Platform for improvement</div>
  <p class="a tiny w" style="left:185px;top:85px;width:125px">Here is a short block of body copy for this slide. It explains the main idea in a few plain sentences and leaves room for detail. Keep the message clear, brief and easy to scan for the reader in the room.</p>
</section>

<!-- 11 Bar chart -->
<section class="slide col2 row4">
  <div class="logo tl"><span class="mark"></span>FlowMarble</div>
  <div class="htitle r">Bullet &amp; Chart Area</div>
  <div class="a" style="left:68px;top:60px;width:1px;height:112px;background:#ddd"></div>
  <div class="a" style="left:33px;top:65px;font-size:4.5px;color:#666">Category 1</div>
  <div class="a" style="left:69px;top:62px;width:52px;height:3px;background:var(--navy)"></div>
  <div class="a" style="left:69px;top:65px;width:63px;height:3px;background:var(--blue)"></div>
  <div class="a" style="left:69px;top:68px;width:45px;height:3px;background:var(--grey)"></div>
  <div class="a" style="left:33px;top:95px;font-size:4.5px;color:#666">Category 2</div>
  <div class="a" style="left:69px;top:92px;width:52px;height:3px;background:var(--navy)"></div>
  <div class="a" style="left:69px;top:95px;width:63px;height:3px;background:var(--blue)"></div>
  <div class="a" style="left:69px;top:98px;width:45px;height:3px;background:var(--grey)"></div>
  <div class="a" style="left:33px;top:125px;font-size:4.5px;color:#666">Category 3</div>
  <div class="a" style="left:69px;top:122px;width:52px;height:3px;background:var(--navy)"></div>
  <div class="a" style="left:69px;top:125px;width:63px;height:3px;background:var(--blue)"></div>
  <div class="a" style="left:69px;top:128px;width:45px;height:3px;background:var(--grey)"></div>
  <div class="a" style="left:33px;top:155px;font-size:4.5px;color:#666">Category 4</div>
  <div class="a" style="left:69px;top:152px;width:52px;height:3px;background:var(--navy)"></div>
  <div class="a" style="left:69px;top:155px;width:63px;height:3px;background:var(--blue)"></div>
  <div class="a" style="left:69px;top:158px;width:45px;height:3px;background:var(--grey)"></div>
  <div class="a bullet c1" style="left:186px;top:61px"><div class="icon hex" style="width:16px;height:18px"><span class="dot"></span></div><div class="t" style="left:27px">Your Text Here</div><p class="b tiny" style="left:27px">Short supporting copy for this point goes here, kept brief to fit two or three lines.</p></div>
  <div class="a bullet c2" style="left:186px;top:90px"><div class="icon hex" style="width:16px;height:18px"><span class="dot"></span></div><div class="t" style="left:27px">Your Text Here</div><p class="b tiny" style="left:27px">Short supporting copy for this point goes here, kept brief to fit two or three lines.</p></div>
  <div class="a bullet c3" style="left:186px;top:119px"><div class="icon hex" style="width:16px;height:18px"><span class="dot"></span></div><div class="t" style="left:27px">Your Text Here</div><p class="b tiny" style="left:27px">Short supporting copy for this point goes here, kept brief to fit two or three lines.</p></div>
  <div class="a bullet c4" style="left:186px;top:147px"><div class="icon hex" style="width:16px;height:18px"><span class="dot"></span></div><div class="t" style="left:27px">Your Text Here</div><p class="b tiny" style="left:27px">Short supporting copy for this point goes here, kept brief to fit two or three lines.</p></div>
</section>

<!-- 12 Agenda on photo band -->
<section class="slide col3 row4">
  <div class="logo tl"><span class="mark"></span>FlowMarble</div>
  <div class="htitle r">Our Agenda</div>
  <div class="band" role="img" aria-label="Blue-tinted photo of a railway platform" style="top:35px;height:151px;background:linear-gradient(100deg,#1f86d4,#1578c2 50%,#2a8fd6)"></div>
  <div class="a agenda inv" style="left:50px;top:47px"><div class="icon hex"><span class="dot"></span></div><div class="t">Lorem Ipsum</div><p class="b tiny w">Short note about this agenda item, kept brief to fit within three small lines of copy.</p></div>
  <div class="a agenda inv" style="left:188px;top:47px"><div class="icon hex"><span class="dot"></span></div><div class="t">Lorem Ipsum</div><p class="b tiny w">Short note about this agenda item, kept brief to fit within three small lines of copy.</p></div>
  <div class="a agenda inv" style="left:50px;top:95px"><div class="icon hex"><span class="dot"></span></div><div class="t">Agenda Two</div><p class="b tiny w">Short note about this agenda item, kept brief to fit within three small lines of copy.</p></div>
  <div class="a agenda inv" style="left:188px;top:95px"><div class="icon hex"><span class="dot"></span></div><div class="t">Lorem Ipsum</div><p class="b tiny w">Short note about this agenda item, kept brief to fit within three small lines of copy.</p></div>
  <div class="a agenda inv" style="left:50px;top:142px"><div class="icon hex"><span class="dot"></span></div><div class="t">Lorem Ipsum</div><p class="b tiny w">Short note about this agenda item, kept brief to fit within three small lines of copy.</p></div>
  <div class="a agenda inv" style="left:188px;top:142px"><div class="icon hex"><span class="dot"></span></div><div class="t">Lorem Ipsum</div><p class="b tiny w">Short note about this agenda item, kept brief to fit within three small lines of copy.</p></div>
</section>

<!-- 13 Team -->
<section class="slide col1 row5">
  <div class="logo tl"><span class="mark"></span>FlowMarble</div>
  <div class="htitle r">Our Team</div>
  <div class="band blue-fill" style="top:48px;height:124px"></div>
  <div class="a" style="left:48px;top:56px;width:60px">
    <div class="hex" style="width:54px;height:60px;margin:0 auto;background:#fff;padding:2px"><div class="hex" role="img" aria-label="Portrait photo of a team member" style="width:50px;height:56px;background:linear-gradient(170deg,#d9dde1,#a38a78 60%,#7a5a4a)"></div></div>
    <div class="center-text" style="font:600 6.5px 'Montserrat',sans-serif;color:#fff;margin-top:5px;white-space:nowrap;width:80px;margin-left:-10px">Dana Whitlock</div>
    <div class="center-text" style="font-size:4.5px;color:#e6f2fc">CEO</div>
    <p class="tiny w center-text" style="margin-top:1px;width:80px;margin-left:-10px">Short line about this person and their role.</p>
  </div>
  <div class="a" style="left:140px;top:56px;width:60px">
    <div class="hex" style="width:54px;height:60px;margin:0 auto;background:#fff;padding:2px"><div class="hex" role="img" aria-label="Portrait photo of a team member" style="width:50px;height:56px;background:linear-gradient(170deg,#d9dde1,#a38a78 60%,#7a5a4a)"></div></div>
    <div class="center-text" style="font:600 6.5px 'Montserrat',sans-serif;color:#fff;margin-top:5px;white-space:nowrap;width:80px;margin-left:-10px">Dana Whitlock</div>
    <div class="center-text" style="font-size:4.5px;color:#e6f2fc">CEO</div>
    <p class="tiny w center-text" style="margin-top:1px;width:80px;margin-left:-10px">Short line about this person and their role.</p>
  </div>
  <div class="a" style="left:234px;top:56px;width:60px">
    <div class="hex" style="width:54px;height:60px;margin:0 auto;background:#fff;padding:2px"><div class="hex" role="img" aria-label="Portrait photo of a team member" style="width:50px;height:56px;background:linear-gradient(170deg,#d9dde1,#a38a78 60%,#7a5a4a)"></div></div>
    <div class="center-text" style="font:600 6.5px 'Montserrat',sans-serif;color:#fff;margin-top:5px;white-space:nowrap;width:80px;margin-left:-10px">Dana Whitlock</div>
    <div class="center-text" style="font-size:4.5px;color:#e6f2fc">CEO</div>
    <p class="tiny w center-text" style="margin-top:1px;width:80px;margin-left:-10px">Short line about this person and their role.</p>
  </div>
</section>

<!-- 14 Column infographic -->
<section class="slide col2 row5">
  <div class="logo tl"><span class="mark"></span>FlowMarble</div>
  <div class="htitle r">About Us</div>
  <div class="band tint-fill" style="top:36px;height:49px"></div>
  <div class="a center-text sec-title" style="left:0;right:0;top:42px">Column Infographic</div>
  <p class="a tiny center-text" style="left:40px;right:40px;top:56px">This chart compares two measures across three groups. Use the space below to explain what the numbers show and why the gap between them matters for the plan.</p>
  <svg class="a" style="left:60px;top:96px" width="240" height="62" viewBox="0 0 240 62">
    <g stroke="#e3e3e3" stroke-width=".5">
      <line x1="18" y1="5" x2="234" y2="5"/><line x1="18" y1="13.5" x2="234" y2="13.5"/><line x1="18" y1="22" x2="234" y2="22"/>
      <line x1="18" y1="30.5" x2="234" y2="30.5"/><line x1="18" y1="39" x2="234" y2="39"/><line x1="18" y1="47.5" x2="234" y2="47.5"/>
    </g>
    <line x1="18" y1="56" x2="234" y2="56" stroke="#999" stroke-width=".6"/>
    <g font-family="Open Sans, sans-serif" font-size="3.2" fill="#666" text-anchor="end">
      <text x="14" y="6">120</text><text x="14" y="14.5">100</text><text x="14" y="23">80</text><text x="14" y="31.5">60</text><text x="14" y="40">40</text><text x="14" y="48.5">20</text><text x="14" y="57">0</text>
    </g>
    <rect x="30.4" y="21.6" width="28.6" height="34.4" fill="var(--navy)"/>
    <rect x="59" y="37.6" width="29" height="18.4" fill="var(--blue)"/>
    <rect x="96" y="21.6" width="29" height="34.4" fill="var(--navy)"/>
    <rect x="125" y="37.6" width="29" height="18.4" fill="var(--blue)"/>
    <rect x="164" y="21.6" width="29" height="34.4" fill="var(--navy)"/>
    <rect x="193" y="37.6" width="29" height="18.4" fill="var(--blue)"/>
    <g font-family="Montserrat, sans-serif" font-size="3" font-weight="600" fill="#fff" text-anchor="middle">
      <text x="44.7" y="53.5">80%</text><text x="73.5" y="53.5">40%</text>
      <text x="110.5" y="53.5">80%</text><text x="139.5" y="53.5">40%</text>
      <text x="178.5" y="53.5">80%</text><text x="207.5" y="53.5">40%</text>
    </g>
  </svg>
  <div class="a" style="left:74px;top:161px;width:110px">
    <div style="display:flex;align-items:center;gap:4px;font:600 4px 'Montserrat',sans-serif;color:var(--navy)"><span class="hex" style="width:5px;height:6px;background:var(--navy)"></span>Column Infographic</div>
    <p class="tiny" style="margin:1px 0 0 9px;width:80px">Short note on this measure, kept to two or three lines.</p>
  </div>
  <div class="a" style="left:200px;top:161px;width:110px">
    <div style="display:flex;align-items:center;gap:4px;font:600 4px 'Montserrat',sans-serif;color:var(--navy)"><span class="hex" style="width:5px;height:6px;background:var(--blue)"></span>Column Infographic</div>
    <p class="tiny" style="margin:1px 0 0 9px;width:80px">Short note on this measure, kept to two or three lines.</p>
  </div>
</section>

<!-- 15 Closing -->
<section class="slide col3 row5" style="background:var(--blue)">
  <div class="logo big" style="top:71px"><span class="mark"></span>FlowMarble</div>
  <div class="band" style="top:145px;height:32px;background:var(--white)"></div>
  <div class="a center-text" style="left:0;right:0;top:153px;font:600 13px 'Montserrat',sans-serif;color:var(--blue)">Thank you for your time</div>
</section>

</body>
</html>
```